R. Talbin Group Business Card

We are looking for a business card mock-up.

Contact Information for Business Card

This is the information that needs to be included:
Name
Title
The R. Talbin Group Inc. Insurance Agents & Brokers (needs to be listed out in entirety)
Logo
License 0482316 (needs to be same sized font as phone number)
Address (728 North Vale Avenue, Los Angeles, CA 90047)
Telephone number ( 714-389-2076 ext. 131)Fax number (714-389-4152)
Email
Website (www.rtalbinagency.example)
Cities (Anaheim, Los Angeles, San Jose, Torrance)

```html
<!DOCTYPE html>
<html lang="en">
<head>
<meta charset="utf-8">
<title>R. Talbin Group Business Card</title>
<link href="https://fonts.googleapis.com/css2?family=Open+Sans:wght@400&family=Tinos:wght@700&display=swap" rel="stylesheet">
<style>
  :root {
    --backdrop: #5c5c5c;
    --paper: #ffffff;
    --copper: #a8693a;
    --copper-light: #b57a4b;
    --ink: #1e1e1e;
    --cream: #f4e6d8;
    --rule: #d9b89c;
  }
  * { margin: 0; padding: 0; box-sizing: border-box; }
  html, body { width: 1200px; height: 900px; overflow: hidden; }
  body {
    position: relative;
    background: var(--backdrop);
    font-family: "Open Sans", Arial, sans-serif;
  }
  .card {
    position: absolute;
    top: 200px;
    width: 310px;
    height: 502px;
    overflow: hidden;
    box-shadow: 3px 4px 6px rgba(0,0,0,0.35);
  }
  .card-front {
    left: 253px;
    background: var(--paper);
    border-radius: 62px 0 62px 0;
  }
  .card-back {
    left: 627px;
    width: 309px;
    background: var(--copper);
    border-radius: 0 62px 0 62px;
    color: var(--cream);
    text-align: center;
  }
  .brand {
    position: absolute;
    left: 40px;
    top: 107px;
    display: flex;
    align-items: center;
    gap: 10px;
  }
  .brand-dot {
    width: 45px; height: 45px;
    border-radius: 50%;
    background: var(--copper);
  }
  .brand-name {
    font-size: 22px;
    color: var(--ink);
    letter-spacing: 0.3px;
  }
  .person {
    position: absolute;
    left: 32px;
    top: 226px;
  }
  .person-name {
    font-family: "Tinos", "Times New Roman", serif;
    font-weight: 700;
    font-size: 18px;
    color: var(--copper);
    letter-spacing: 0.3px;
    line-height: 20px;
  }
  .person-title {
    font-size: 14.5px;
    color: var(--ink);
    line-height: 18px;
  }
  .contacts {
    position: absolute;
    left: 33px;
    top: 274px;
    list-style: none;
    font-size: 14.5px;
    line-height: 18.2px;
    color: var(--ink);
  }
  .contacts li { display: flex; align-items: center; gap: 5px; }
  .contacts svg { width: 12px; height: 12px; fill: var(--copper); flex: none; }
  .office {
    position: absolute;
    left: 33px;
    top: 356px;
    font-size: 14.5px;
    line-height: 18.2px;
    color: var(--ink);
  }
  .office .agency { color: var(--copper); }
  .license {
    position: absolute;
    left: 34px;
    top: 446px;
    font-size: 14.5px;
    color: var(--ink);
  }
  .world-map {
    position: absolute;
    left: 0; top: 0;
    width: 309px; height: 220px;
    background: radial-gradient(ellipse at 55% 45%, rgba(214,160,118,0.55), rgba(214,160,118,0.15) 70%, rgba(214,160,118,0) 100%);
  }
  .cities {
    position: absolute;
    left: 0; right: 0;
    top: 230px;
    font-size: 16px;
    line-height: 20px;
  }
  .divider {
    position: absolute;
    left: 35px;
    width: 239px;
    top: 353px;
    height: 1px;
    background: var(--rule);
  }
  .services {
    position: absolute;
    left: 0; right: 0;
    top: 382px;
    list-style: none;
    font-size: 16px;
    line-height: 20.3px;
  }
</style>
</head>
<body>
  <section class="card card-front">
    <div class="brand">
      <span class="brand-dot"></span>
      <span class="brand-name">R. Talbin Group</span>
    </div>

    <div class="person">
      <p class="person-name">DANIEL HARPER</p>
      <p class="person-title">Managing Director</p>
    </div>

    <ul class="contacts">
      <li>
        <svg viewBox="0 0 12 12"><path d="M1 4c0-2 2-3 5-3s5 1 5 3v1H8V4H4v1H1zM3 6h6l2 5H1z"/></svg>
        714-389-2076 ext. 131
      </li>
      <li>
        <svg viewBox="0 0 12 12"><path d="M3 1h6v3H3zM1 5h10v5H9v-2H3v2H1zM4 9h4v2H4z"/></svg>
        714-389-4152
      </li>
      <li>
        <svg viewBox="0 0 12 12"><path d="M1 2.5h10v7H1zM1.8 3.2 6 6.5l4.2-3.3"/><path d="M1.5 3 6 6.6 10.5 3" fill="none" stroke="#fff" stroke-width="0.9"/></svg>
        info@rtalbinagency.example
      </li>
      <li>
        <svg viewBox="0 0 12 12"><circle cx="6" cy="6" r="5.5"/><path d="M3 4c1 0 2 1 1.5 2S5 8 4 9.5M7 2c0 1.5 2 1 2.5 2.5S8 7 8 9" fill="none" stroke="#fff" stroke-width="0.9"/></svg>
        www.rtalbinagency.example
      </li>
    </ul>

    <div class="office">
      <p class="agency">The R. Talbin Group Inc.</p>
      <p class="agency">Insurance Agents &amp; Brokers</p>
      <p>728 North Vale Avenue</p>
      <p>Los Angeles, CA 90047</p>
    </div>

    <p class="license">LICENSE 0482316</p>
  </section>

  <section class="card card-back">
    <div class="world-map" role="img" aria-label="Dotted world map"></div>
    <p class="cities">Anaheim | Los Angeles<br>San Jose | Torrance</p>
    <div class="divider"></div>
    <ul class="services">
      <li>Business Insurance</li>
      <li>Workers' Comp Insurance</li>
      <li>Auto Insurance</li>
      <li>Home Insurance</li>
    </ul>
  </section>
</body>
</html>
```